Freelance Makeup Artist Needing Business Card Design

I am a freelance makeup artist looking for a design for my business cards.
My target audience is people looking for bridal makeup, so i was thinking minimalistic style, black with white or gold foil accents.
Something that feels classy but simple and to the point.

I would like the front to state Marisa Pelworth and Makeup Artist, and the back to include my social media and contact details.

Target Market(s)

Brides, young women

Industry/Entity Type

Business

Contact Information for Business Card

0417352840
marisa.pelworth@quorvel.com
www.snapvale.com/marisa.pelworth
www.friendloop.com/MarisaPelworthMakeup

Requirements
Nice to have
• Social media icons next to relevant contact details

```html
<!DOCTYPE html>
<html lang="en">
<head>
<meta charset="utf-8">
<title>Marisa Pelworth – Makeup Artist Business Card</title>
<link href="https://fonts.googleapis.com/css2?family=Great+Vibes&family=Cinzel:wght@500&family=Montserrat:wght@500&display=swap" rel="stylesheet">
<style>
  :root {
    --backdrop: #8e8e8e;
    --gold-light: #e8c75a;
    --gold-mid: #d1a62c;
    --gold-deep: #b78a1c;
    --ink: #141210;
    --card-black: #0d0c0b;
    --foil-hi: #f3d77f;
    --foil-lo: #a97d1f;
  }
  * { margin: 0; padding: 0; box-sizing: border-box; }
  html, body { width: 1200px; height: 872px; overflow: hidden; }
  body { background: var(--backdrop); position: relative; font-family: "Montserrat", sans-serif; }

  .card {
    position: absolute;
    width: 560px;
    height: 320px;
    border-radius: 3px;
    box-shadow: 0 14px 30px rgba(0,0,0,.35);
    overflow: hidden;
  }

  /* Back side */
  .card-back {
    left: 560px; top: 70px;
    background: linear-gradient(135deg, var(--gold-light), var(--gold-mid) 55%, var(--gold-deep));
    color: var(--ink);
  }
  .floral-texture {
    position: absolute; inset: 0;
    background: radial-gradient(circle at 40% 40%, rgba(255,240,180,.25), rgba(160,120,20,.12) 70%);
  }
  .back-brand {
    position: absolute; left: 36px; top: 108px; width: 260px; text-align: center;
  }
  .back-brand .name { font-family: "Great Vibes", cursive; font-size: 42px; line-height: 1; }
  .back-brand .role { font-family: "Cinzel", serif; font-size: 11px; letter-spacing: 4px; margin-top: 4px; }
  .divider {
    position: absolute; left: 318px; top: 40px; width: 1.5px; height: 240px; background: var(--ink);
  }
  .contact-list {
    position: absolute; left: 338px; top: 52px; list-style: none; font-size: 12.5px;
  }
  .contact-list li { display: flex; align-items: center; gap: 9px; height: 30px; }
  .contact-list .icon { width: 16px; height: 16px; flex: none; }
  .contact-list .dot { width: 12px; height: 12px; border-radius: 50%; background: var(--ink); flex: none; margin: 0 2px; }
  .contact-list .net { font-size: 9px; letter-spacing: .5px; margin-right: -3px; }
  .contact-list .addr { line-height: 1.2; font-size: 12px; }
  .contact-list li.tall { height: 40px; }

  /* Front side */
  .card-front {
    left: 80px; top: 470px;
    background: var(--card-black);
  }
  .card-front .floral-texture {
    background: radial-gradient(circle at 50% 50%, rgba(60,55,50,.35), rgba(0,0,0,0) 75%);
  }
  .front-brand {
    position: absolute; inset: 0; display: flex; flex-direction: column; align-items: center; justify-content: center;
  }
  .foil {
    background: linear-gradient(180deg, var(--foil-hi), var(--gold-mid) 55%, var(--foil-lo));
    -webkit-background-clip: text; background-clip: text; color: transparent;
  }
  .front-brand .name { font-family: "Great Vibes", cursive; font-size: 74px; line-height: 1.1; }
  .front-brand .role { font-family: "Cinzel", serif; font-size: 20px; letter-spacing: 7px; margin-top: 6px; }
</style>
</head>
<body>

<section class="card card-back">
  <div class="floral-texture" role="img" aria-label="Faint tone-on-tone floral line pattern"></div>
  <div class="back-brand">
    <div class="name">Marisa Pelworth</div>
    <div class="role">MAKEUP ARTIST</div>
  </div>
  <div class="divider"></div>
  <ul class="contact-list">
    <li><span class="dot"></span><span class="net">Snapvale</span><span>@marisa.pelworth</span></li>
    <li><span class="dot"></span><span class="net">Friendloop</span><span>Marisa Pelworth</span></li>
    <li><span class="dot"></span><span class="net">Chirpline</span><span>@marisa.pelworth</span></li>
    <li>
      <svg class="icon" viewBox="0 0 24 24"><path fill="currentColor" d="M6.6 10.8a15.1 15.1 0 0 0 6.6 6.6l2.2-2.2a1 1 0 0 1 1-.25 11.4 11.4 0 0 0 3.6.57 1 1 0 0 1 1 1V20a1 1 0 0 1-1 1A17 17 0 0 1 3 4a1 1 0 0 1 1-1h3.5a1 1 0 0 1 1 1c0 1.25.2 2.45.57 3.57a1 1 0 0 1-.25 1z"/></svg>
      <span>0417352840</span>
    </li>
    <li class="tall">
      <svg class="icon" viewBox="0 0 24 24"><path fill="none" stroke="currentColor" stroke-width="2.2" d="M12 22s-7-7.2-7-12.5a7 7 0 0 1 14 0C19 14.8 12 22 12 22z"/><circle cx="12" cy="9.5" r="2.5" fill="currentColor"/></svg>
      <span class="addr">City Name Here, 5690<br>Street Address Here, No 323</span>
    </li>
    <li>
      <svg class="icon" viewBox="0 0 24 24"><rect x="2.5" y="5" width="19" height="14" fill="none" stroke="currentColor" stroke-width="1.8"/><path d="M2.5 5l9.5 8 9.5-8" fill="none" stroke="currentColor" stroke-width="1.8"/></svg>
      <span>marisa.pelworth@quorvel.com</span>
    </li>
  </ul>
</section>

<section class="card card-front">
  <div class="floral-texture" role="img" aria-label="Subtle dark floral line pattern"></div>
  <div class="front-brand">
    <div class="name foil">Marisa Pelworth</div>
    <div class="role foil">MAKEUP ARTIST</div>
  </div>
</section>

</body>
</html>
```